Brightwell Support! Virtual Assistant business needs a Website

I have started an online business called "Brightwell Support". I offer all the same types of services as a typical Personal Assistant, only remotely. For example, document formatting and editing (word, powerpoint, excel etc.), email and calendar management, appointments and bookings, document creation, reports, travel and event management and so on.

I already have a logo ready to go, however I have yet to finalise the copy for the site, so if you could create the pages with pictures, and I can fill in the wording at a later date.

Target Market(s)

Anyone who is overloaded at work and needs someone to take the admin work off their hands.

Number of Pages Required

4 page

Font styles to use
Sans Serif
Script
Other font styles liked:
• Gotham Medium is used in my font

Colors

Designer to choose colors to be used in the design.

Requirements
Must have
• Home Page
• About Page
• Pricing Page
• Contact Page
Nice to have
• Pictures and a professional design, I like white space and simple design.
Should not have
• cartoons or anything unprofessional looking.

```html
<!DOCTYPE html>
<html lang="en">
<head>
<meta charset="utf-8">
<title>Brightwell Support</title>
<link href="https://fonts.googleapis.com/css2?family=Montserrat:wght@300;400;500;600;700;800&display=swap" rel="stylesheet">
<style>
:root{
  --blue:#1f5fae;
  --sky:#14a0f0;
  --deep:#1e4fa3;
  --ink:#222;
  --muted:#8a8a8a;
  --grey:#98999c;
  --band:#f3f3f4;
  --dark:#1d1f22;
  --white:#fff;
}
*{margin:0;padding:0;box-sizing:border-box}
html,body{width:1200px;height:2965px;overflow:hidden}
body{font-family:"Montserrat",Arial,sans-serif;color:var(--ink);background:var(--white);position:relative}
.abs{position:absolute}

/* hero */
.hero{left:0;top:0;width:1200px;height:731px;background:linear-gradient(120deg,#2a2d31 0%,#1b1d20 55%,#2b2e33 100%);overflow:hidden}
.hero-accent{left:0;top:0}
.brand{display:flex;align-items:center;gap:12px}
.brand-dot{width:70px;height:70px;border-radius:50%;background:var(--blue);flex:none}
.brand-name{font-weight:600;font-size:22px;color:var(--blue);letter-spacing:0.5px;text-transform:uppercase;white-space:nowrap}
.hero .brand{left:79px;top:25px}
.nav{top:45px;left:654px;font-size:13px;color:#8c8f94;text-transform:uppercase}
.nav a{color:inherit;text-decoration:none;position:absolute;white-space:nowrap}
.nav a.active{color:var(--white)}
.search{left:1073px;top:31px;width:48px;height:48px;border-radius:50%;background:#3d4045;border:2px solid #5a5d62}
.hero-photo{left:640px;top:158px;width:408px;height:603px;border-radius:200px 200px 40px 40px;background:linear-gradient(180deg,#d8b9a2 0%,#f0d9cf 40%,#4c6d96 75%,#3b5a80 100%);z-index:1}
.hero-title{left:79px;top:236px;font-size:38px;color:var(--white);font-weight:300;white-space:nowrap;z-index:2}
.hero-title b{font-weight:800}
.hero-sub{left:79px;top:287px;font-size:26px;font-weight:700;color:var(--sky);letter-spacing:2px;z-index:2}
.hero-text{left:79px;top:343px;width:560px;font-size:14.5px;line-height:20px;color:#e6e6e6;z-index:2}
.pill{display:flex;align-items:center;justify-content:space-between;height:58px;border-radius:29px;background:var(--white);padding-left:32px;font-size:16px;font-weight:500;color:var(--ink);text-transform:uppercase;box-shadow:0 2px 6px rgba(0,0,0,.15)}
.pill-dot{width:54px;height:54px;border-radius:50%;background:linear-gradient(135deg,#2c6fbf,#173d7a);margin-right:2px;border:3px solid #e4e9f1}
.pill-outline{border:2px solid #d8d8d8;box-shadow:none}
.hero-btn{left:79px;top:429px;width:336px;z-index:2}

/* services */
.services{left:0;top:731px;width:1200px;height:327px;background:var(--band)}
.service{width:230px;text-align:center;top:80px}
.service-ring{width:126px;height:126px;border-radius:50%;margin:0 auto;background:var(--white);border:4px solid #cfd1d4;display:flex;align-items:center;justify-content:center;box-shadow:0 3px 8px rgba(0,0,0,.08)}
.service-ring.on{border-color:#2a78d0}
.service-label{margin-top:20px;font-size:17px;line-height:20px;color:var(--deep)}
.service-label.dark{color:var(--ink)}
.service-rule{width:200px;height:1px;margin:22px auto 0;background:linear-gradient(90deg,transparent,#dcdcdc,transparent)}

/* welcome */
.welcome-title{left:0;top:1124px;width:1200px;text-align:center;font-size:45px;font-weight:400;color:var(--blue);letter-spacing:2px;text-transform:uppercase}
.welcome-text{left:170px;top:1196px;width:860px;text-align:center;font-size:14px;line-height:23px;color:var(--muted)}
.welcome-btn{left:486px;top:1309px;width:226px;color:var(--deep)}

/* pricing */
.pricing{left:0;top:1443px;width:1200px;height:530px;background:var(--band)}
.pricing-title{left:0;top:71px;width:1200px;text-align:center;font-size:44px;font-weight:400;color:var(--blue);text-transform:uppercase;letter-spacing:1px}
.plan{color:var(--white);text-align:center}
.plan-head{height:52px;line-height:52px;font-size:18px}
.plan-body{padding-top:24px}
.plan-price{font-size:34px;font-weight:700}
.plan-rule{width:70%;height:1px;background:rgba(255,255,255,.3);margin:22px auto 20px}
.plan-item{font-size:13px;line-height:32px}
.plan-cta{display:inline-block;margin-top:12px;font-size:15px;font-weight:700;text-decoration:underline;letter-spacing:1px}
.h-blue{background:var(--deep);color:var(--white)}
.h-grey{background:var(--grey);color:var(--ink)}
.b-grey{background:var(--grey)}
.b-blue{background:var(--deep)}

/* contact */
.contact{left:0;top:1973px;width:1200px;height:627px;background:var(--white);overflow:hidden}
.contact-photo{left:237px;top:63px;width:336px;height:564px;border-radius:160px 160px 0 0;background:linear-gradient(180deg,#4a3328 0%,#b88a6e 30%,#e9e3dc 60%,#8b7a6b 100%)}
.contact-title{left:603px;top:73px;font-size:46px;font-weight:400;color:var(--blue);letter-spacing:2px;text-transform:uppercase}
.contact-sub{left:603px;top:148px;font-size:26px;line-height:36px;color:var(--ink)}
.contact-sub span{color:var(--muted)}
.field{height:50px;border:2px solid #e6e6e6;border-radius:25px;display:flex;align-items:center;padding-left:22px;gap:10px;font-size:13px;color:#b8b8b8;background:var(--white)}
.field i{width:16px;height:16px;border:1.5px solid #c9c9c9;border-radius:50%;display:block}
.submit{left:771px;top:2420px;width:178px;color:var(--deep)}

/* footer */
.footer{left:0;top:2600px;width:1200px;height:365px;background:linear-gradient(180deg,#2a2c30,#1b1d20)}
.footer .brand{left:79px;top:55px;gap:8px}
.footer .brand-dot{width:56px;height:56px}
.footer .brand-name{font-size:16px;letter-spacing:0}
.footer-about{left:79px;top:137px;width:180px;font-size:12px;line-height:17px;color:#8e9096}
.social{top:218px;width:42px;height:42px;border-radius:50%;border:2px solid #c8c8c8}
.social.fill{background:var(--white)}
.f-head{top:63px;font-size:18px;font-weight:400;color:var(--sky)}
.f-links{left:346px;top:100px;list-style:none;font-size:15px;line-height:27px;color:#a3a5aa}
.f-links li::before{content:"›";margin-right:12px;color:#a3a5aa}
.f-info{font-size:14px;line-height:20px;color:#b6b8bc}
.f-info svg{position:absolute;left:0;top:2px}
.f-email{left:870px;top:105px;width:252px;height:50px;border:2px solid #cfd0d2;border-radius:25px;padding-left:30px;line-height:46px;font-size:13px;color:#9a9ca0}
.f-sub{left:866px;top:167px;width:256px}
.f-line{left:79px;top:312px;width:1043px;height:1px;background:#3d4045}
.copyright{left:0;top:330px;width:1200px;text-align:center;font-size:14px;color:#a3a5aa}
.copyright b{color:var(--white);text-transform:uppercase}
</style>
</head>
<body>

<section class="hero abs">
  <svg class="hero-accent abs" width="1200" height="731" viewBox="0 0 1200 731">
    <polygon points="1060,0 1200,0 1200,731 640,731" fill="#14a0f0"/>
    <polygon points="1200,240 1200,731 900,731" fill="#0d8ee0"/>
  </svg>
  <div class="brand abs"><span class="brand-dot"></span><span class="brand-name">Brightwell Support</span></div>
  <nav class="nav abs">
    <a class="active" style="left:0">Home</a>
    <a style="left:81px">About Us</a>
    <a style="left:192px">Pricing</a>
    <a style="left:287px">Contact Us</a>
  </nav>
  <div class="search abs"></div>
  <div class="hero-photo abs" role="img" aria-label="Photo of a smiling woman sitting cross-legged with a laptop, pointing to the headline"></div>
  <h1 class="hero-title abs">Finally, a <b>VIRTUAL ASSISTANCE</b></h1>
  <p class="hero-sub abs">for your Recruiters!</p>
  <p class="hero-text abs">Stop trying to do it all.Let BRIGHTWELL SUPPORT automate tedious, time-consuming tasks including manual resume screening and candidate sourcing.</p>
  <a class="pill hero-btn abs">Request our assistant<span class="pill-dot"></span></a>
</section>

<section class="services abs">
  <div class="service abs" style="left:75px">
    <div class="service-ring on">
      <svg width="60" height="60" viewBox="0 0 60 60" fill="none" stroke="#1e4fa3" stroke-width="2.5"><path d="M14 8h24l8 8v36H14z"/><path d="M20 22h18M20 30h18M20 38h10"/><path d="M36 46l12-14 4 4-12 14-5 1z"/></svg>
    </div>
    <p class="service-label dark">Document Formatting<br>and Editing</p>
    <div class="service-rule"></div>
  </div>
  <div class="service abs" style="left:352px">
    <div class="service-ring">
      <svg width="60" height="60" viewBox="0 0 60 60" fill="none" stroke="#1e4fa3" stroke-width="2.5"><rect x="10" y="10" width="30" height="28"/><path d="M10 17h30M16 6v8M34 6v8M15 23h4M23 23h4M31 23h4M15 30h4M23 30h4"/><rect x="24" y="32" width="28" height="20"/><path d="M24 32l14 11 14-11"/></svg>
    </div>
    <p class="service-label">Email and Calendar<br>Management</p>
    <div class="service-rule"></div>
  </div>
  <div class="service abs" style="left:622px">
    <div class="service-ring">
      <svg width="60" height="60" viewBox="0 0 60 60" fill="none" stroke="#1e4fa3" stroke-width="2.5"><rect x="8" y="12" width="44" height="38" rx="3"/><path d="M8 21h44M18 7v9M42 7v9"/><g fill="#1e4fa3" stroke="none"><rect x="14" y="26" width="6" height="5"/><rect x="24" y="26" width="6" height="5"/><rect x="34" y="26" width="6" height="5"/><rect x="14" y="36" width="6" height="5"/><rect x="24" y="36" width="6" height="5"/><rect x="34" y="36" width="6" height="5"/></g></svg>
    </div>
    <p class="service-label">Appointments And<br>Bookings</p>
    <div class="service-rule"></div>
  </div>
  <div class="service abs" style="left:893px">
    <div class="service-ring">
      <svg width="60" height="60" viewBox="0 0 60 60" fill="none" stroke="#1e4fa3" stroke-width="2.5"><path d="M22 6h18l8 8v30H22z"/><path d="M16 14v36h24"/><path d="M28 20h14M28 27h14M28 34h14"/></svg>
    </div>
    <p class="service-label" style="margin-top:30px">Document Creation</p>
    <div class="service-rule"></div>
  </div>
</section>

<h2 class="welcome-title abs">Welcome to Brightwell Support</h2>
<p class="welcome-text abs">Lorem ipsum has been the industry's standard dummy text ever since the 1500s, when an unknown printer took a galley of type and scrambled it to make a type specimen book.It has survived not only five centuries.Lorem Ipsum has been the industry's standard dummy text ever since the 1500s, when an unknown printer took a galley of type and scrambled it to make a type specimen book.It has survived not only five centuries.</p>
<a class="pill pill-outline welcome-btn abs">Learn more<span class="pill-dot"></span></a>

<section class="pricing abs">
  <h2 class="pricing-title abs">Our Pricing</h2>
  <div class="plan abs" style="left:77px;top:162px;width:257px">
    <div class="plan-head h-blue">Entrepreneur Plan</div>
    <div class="plan-body b-grey" style="height:227px">
      <div class="plan-price">$299</div><div class="plan-rule"></div>
      <div class="plan-item">• 12 hours per month</div><div class="plan-item">• 1 User Included</div>
    </div>
  </div>
  <div class="plan abs" style="left:334px;top:145px;width:273px">
    <div class="plan-head h-grey">Startup Plan</div>
    <div class="plan-body b-blue" style="height:263px;padding-top:14px">
      <div class="plan-price">$ 599</div><div class="plan-rule"></div>
      <div class="plan-item">• 24 hours per month</div><div class="plan-item">• 2 User Included</div>
      <a class="plan-cta">START TRIAL</a>
    </div>
  </div>
  <div class="plan abs" style="left:607px;top:162px;width:255px">
    <div class="plan-head h-blue">Small Business Plan</div>
    <div class="plan-body b-grey" style="height:227px;padding-top:14px">
      <div class="plan-price">$899</div><div class="plan-rule"></div>
      <div class="plan-item">• 36 hours per month</div><div class="plan-item">• 3 User Included</div>
    </div>
  </div>
  <div class="plan abs" style="left:862px;top:162px;width:261px">
    <div class="plan-head h-grey">Team Plan</div>
    <div class="plan-body b-blue" style="height:227px;padding-top:44px">
      <div class="plan-price">$1199</div><div class="plan-rule"></div>
      <div class="plan-item">• 50 hours per month</div><div class="plan-item">• 5 User Included</div>
    </div>
  </div>
</section>

<section class="contact abs">
  <svg class="abs" style="left:0;top:0" width="600" height="627" viewBox="0 0 600 627">
    <polygon points="0,0 200,0 560,627 0,627" fill="#14a0f0"/>
    <polygon points="0,260 0,627 420,627" fill="#0d8ee0"/>
  </svg>
  <div class="contact-photo abs" role="img" aria-label="Photo of a smiling businesswoman in a white blazer holding a phone"></div>
  <h2 class="contact-title abs">Contact Us</h2>
  <p class="contact-sub abs">Tell us what you need <span>so you can<br>meet your virtual assistant.</span></p>
  <div class="field abs" style="left:603px;top:250px;width:251px"><i></i>For my business</div>
  <div class="field abs" style="left:870px;top:250px;width:253px"><i></i>Company</div>
  <div class="field abs" style="left:603px;top:313px;width:251px"><i></i>First Name</div>
  <div class="field abs" style="left:870px;top:313px;width:253px"><i></i>Last Name</div>
  <div class="field abs" style="left:603px;top:378px;width:520px"><i></i>Email Id</div>
</section>
<a class="pill pill-outline submit abs">Submit<span class="pill-dot"></span></a>

<footer class="footer abs">
  <div class="brand abs"><span class="brand-dot"></span><span class="brand-name">Brightwell Support</span></div>
  <p class="footer-about abs">Lorem ipsum has been the industry's standard dummy text ever since the 1500.</p>
  <span class="social fill abs" style="left:76px"></span>
  <span class="social abs" style="left:127px"></span>
  <span class="social abs" style="left:181px"></span>
  <span class="social abs" style="left:232px"></span>

  <h3 class="f-head abs" style="left:346px">Usefull Links</h3>
  <ul class="f-links abs"><li>Home</li><li>About Us</li><li>Pricing</li><li>Services</li><li>Contact Us</li></ul>

  <h3 class="f-head abs" style="left:605px">Contact Info</h3>
  <div class="f-info abs" style="left:605px;top:100px;width:230px;padding-left:26px">
    <svg width="16" height="20" viewBox="0 0 16 20" fill="none" stroke="#14a0f0" stroke-width="1.6"><path d="M8 19s6-7 6-11A6 6 0 0 0 2 8c0 4 6 11 6 11z"/><circle cx="8" cy="8" r="2.2"/></svg>
    123,Consectetur adipiscing,<br>sed do eiusmod tempor,<br>quis nostrud
  </div>
  <div class="f-info abs" style="left:605px;top:196px;width:230px;padding-left:26px">
    <svg width="18" height="18" viewBox="0 0 18 18" fill="none" stroke="#14a0f0" stroke-width="1.6"><path d="M4 1l3 4-2 2c1 3 3 5 6 6l2-2 4 3-2 3C8 17 1 10 1 3z"/></svg>
    +123 456 7878
  </div>
  <div class="f-info abs" style="left:605px;top:235px;width:260px;padding-left:26px">
    <svg width="18" height="14" viewBox="0 0 18 14" fill="none" stroke="#14a0f0" stroke-width="1.6"><rect x="1" y="1" width="16" height="12"/><path d="M1 1l8 7 8-7"/></svg>
    info@brightwellsupport.com
  </div>

  <h3 class="f-head abs" style="left:870px">Newsletter</h3>
  <div class="f-email abs">Email</div>
  <a class="pill f-sub abs">Subscribe<span class="pill-dot"></span></a>

  <div class="f-line abs"></div>
  <p class="copyright abs">© <b>Brightwell Support</b> - 2018. All Rights Reserved.</p>
</footer>

</body>
</html>
```